Business Card Design

Take existing logo/brand and develop business card for sales team.
We have two separate brands and require a business card for each.

1. VoxHarbor
2. Kestrava

Refer to our websites www.voxharbor.example.au and www.mynimbuslinko.example.au for designs currently implemented and in the marketplace.

Both cards are brands of our parent company Quorra Systems Pty Ltd - an Australian Telecommunications company in the medium business sector. We have only business customers, no retail/residential consumers.

Target Market(s)

Australian Business - small to medium enterprise

Industry/Entity Type

Business

Contact Information for Business Card

Lev Dorrit
Sales Director
Mobile: +61 400 555 187
Direct: +61 3 9555 0137
Email: lev@voxharbor.example.au
VoxHarbor (a brand of Quorra Systems Pty Ltd)

Lev Dorrit
Sales Director
Mobile: +61 400 555 187
Direct: +61 3 9555 0137
Email: lev@kestrava.example.au
Kestrava (a brand of Quorra Systems Pty Ltd)

Font styles to use
Sans Serif
Other font styles liked:
• Roboto Condensed, Open Sans

Requirements
Must have
• Clean lines, crisp fonts - suggest Roboto Condensed or similar.
• Must be easy to read and clear.
• Brand colour #0C8CCD
• Two colour maximum
Nice to have
• Modern, intellectual and unique design.
Should not have
• No die cuts
• No copies or rip-offs of other designs

```html
<!DOCTYPE html>
<html lang="en">
<head>
<meta charset="utf-8">
<title>Kestrava Business Card</title>
<link rel="stylesheet" href="https://fonts.googleapis.com/css2?family=Roboto:wght@400;500;700&display=swap">
<style>
  :root {
    --brand-blue: #0c8ccd;
    --brand-blue-light: #1eb0e4;
    --brand-blue-deep: #0a72ad;
    --ink: #3d3f42;
    --paper: #ffffff;
    --paper-shade: #eef0f2;
    --backdrop: #2a2c2e;
    --muted-chip: #dfe3e6;
    --muted-text: #a9cfe6;
  }
  * { box-sizing: border-box; margin: 0; padding: 0; }
  html, body {
    width: 1200px;
    height: 900px;
    overflow: hidden;
    background: var(--backdrop);
    font-family: "Roboto", sans-serif;
  }
  .stage {
    position: relative;
    width: 1200px;
    height: 900px;
  }
  .card {
    position: absolute;
    left: 280px;
    width: 640px;
    height: 390px;
    overflow: hidden;
    box-shadow: 0 12px 30px rgba(0,0,0,0.45);
  }
  .card--back {
    top: 40px;
    background: radial-gradient(circle at 42% 40%, var(--brand-blue-light) 0%, var(--brand-blue) 55%, var(--brand-blue-deep) 100%);
  }
  .card--front {
    top: 470px;
    background: linear-gradient(180deg, var(--paper) 0%, var(--paper-shade) 100%);
  }
  .brand-band {
    position: absolute;
    left: 300px;
    right: 0;
    top: 232px;
    height: 68px;
    background: var(--paper);
    border-radius: 34px 0 0 34px;
    display: flex;
    align-items: center;
    padding-left: 30px;
  }
  .wordmark {
    display: flex;
    align-items: center;
    gap: 10px;
  }
  .wordmark__square {
    width: 30px;
    height: 30px;
    background: var(--brand-blue);
  }
  .wordmark__name {
    font-weight: 400;
    font-size: 30px;
    color: var(--ink);
  }
  .card--front .wordmark {
    position: absolute;
    right: 46px;
    top: 86px;
  }
  .card--front .wordmark__square { width: 38px; height: 38px; }
  .card--front .wordmark__name { font-size: 36px; }
  .contact-band {
    position: absolute;
    inset: 0;
    width: 640px;
    height: 390px;
  }
  .person {
    position: absolute;
    left: 40px;
    top: 118px;
  }
  .person__name {
    font-weight: 700;
    font-size: 17px;
    color: var(--brand-blue);
  }
  .person__role {
    font-size: 16px;
    color: var(--ink);
    margin-top: 2px;
  }
  .contact-list {
    position: absolute;
    left: 40px;
    top: 252px;
    display: grid;
    grid-template-columns: 80px auto;
    row-gap: 6px;
    color: var(--paper);
    font-size: 18px;
  }
  .parent-note {
    position: absolute;
    right: 46px;
    top: 246px;
    text-align: right;
    font-size: 12px;
    line-height: 1.35;
    color: var(--muted-text);
  }
  .parent-note strong { font-weight: 700; }
  .corner-chip {
    position: absolute;
    right: 0;
    top: 232px;
    width: 30px;
    height: 30px;
    background: var(--muted-chip);
  }
</style>
</head>
<body>
<main class="stage">
  <section class="card card--back" aria-label="Card back">
    <div class="brand-band">
      <div class="wordmark">
        <span class="wordmark__square"></span>
        <span class="wordmark__name">Kestrava</span>
      </div>
    </div>
  </section>

  <section class="card card--front" aria-label="Card front">
    <svg class="contact-band" viewBox="0 0 640 390" aria-hidden="true">
      <defs>
        <linearGradient id="bandFill" x1="0" y1="0" x2="1" y2="1">
          <stop offset="0" stop-color="#1a9fd8"/>
          <stop offset="1" stop-color="#0a78b6"/>
        </linearGradient>
      </defs>
      <polygon points="0,168 640,222 640,390 0,390" fill="url(#bandFill)"/>
    </svg>

    <div class="wordmark">
      <span class="wordmark__square"></span>
      <span class="wordmark__name">Kestrava</span>
    </div>

    <div class="person">
      <p class="person__name">Lev Dorrit</p>
      <p class="person__role">Sales Director</p>
    </div>

    <dl class="contact-list">
      <dt>Mobile:</dt><dd>+61 400 555 187</dd>
      <dt>Direct:</dt><dd>+61 395 550 137</dd>
      <dt>Email:</dt><dd>lev@kestrava.example.au</dd>
    </dl>

    <p class="parent-note"><strong>Kestrava</strong> a brand of<br>Quorra Systems Pty Ltd</p>
    <span class="corner-chip"></span>
  </section>
</main>
</body>
</html>
```